Skill Up Salary Up

Full Page
7.5 w x 10 h / 8 w x 10.75 h + .25" bleed
Full-Page Career Course Ad
Project Overview
• Goal: Create a visually attractive, modern, and uncluttered full-page magazine advertisement to list available career courses.
• Tone: Creative, professional, and attention-grabbing to prevent the reader from turning the page. The final design must prioritize readability.

Content Requirements
1. Header/Headline: Must be the primary focus. And grab peoples attention
2. Course Listing: A clear, well-organized list of the career courses.
________________________________________
Design & Aesthetic Directives
1. Layout & Readability (Crucial)
• The final ad must not look crowded or busy.
• Prioritize white space to make the text "breathe" and ensure the course list is easy to scan and read.
• Use a modern, clean, and professional typeface (font choice is critical for the aesthetic).
2. Visual Style
• Aim for a creative, modern, and fresh look. Avoid outdated or generic stock imagery/layouts.
3. Imagery/Graphic Element (Artist's Choice)
You have creative freedom regarding the main graphic element.
• Option A (Photography): Use a photo of a white male American with a collared shirt. The imagery should convey success, focus, or professional development.
• Option B (Vector/Illustration): Use a modern vector graphic, illustration, or abstract design. This could be used to symbolize growth, connection, or a career path.
The choice of graphic element is yours, but it must support the overall modern and uncrowded aesthetic.

Requirements
Must have
• Partial listing .. is part of the Harbor Lantern Course

```html
<!DOCTYPE html>
<html lang="en">
<head>
<meta charset="utf-8">
<title>Skill Up, Salary Up – Course Ad</title>
<link rel="stylesheet" href="https://fonts.googleapis.com/css2?family=Poppins:wght@400;500;600;700;800&family=Bebas+Neue&family=Oswald:wght@600;700&display=swap">
<style>
:root{
  --sky:#1e95d9;
  --navy:#22338a;
  --ice:#eef6fb;
  --white:#ffffff;
  --amber:#eea21e;
  --ink:#1c1c2a;
  --stage:#a3a3a3;
}
*{box-sizing:border-box;margin:0;padding:0}
html,body{width:1200px;height:1117px;overflow:hidden}
body{background:var(--stage);font-family:"Poppins",sans-serif;position:relative}
.page{position:absolute;top:226px;width:831px;height:1100px;transform:scale(.6036);transform-origin:0 0;overflow:hidden;background:var(--ice)}
.page--front{left:86px}
.page--back{left:613px}
.abs{position:absolute}
.photo{position:absolute;background:linear-gradient(135deg,#8fb0c8,#dbe6ef 55%,#6c8aa2)}
.card{position:absolute;background:var(--white);border-radius:18px;box-shadow:0 6px 14px rgba(0,0,0,.18)}
.card__title{position:absolute;left:9px;right:9px;top:8px;background:var(--navy);color:var(--white);border-radius:10px;font-weight:700;font-size:28px;line-height:29px;padding:9px 0 9px 25px;text-transform:uppercase}
.blue{color:var(--sky)}
.amber{color:var(--amber)}
.navy{color:var(--navy)}
.tag{position:absolute;background:var(--amber);color:var(--white);font-weight:700;text-align:center;border-radius:3px;text-transform:uppercase}
.outline{position:absolute;border:2px solid var(--amber);border-radius:5px;color:var(--navy);font-weight:700;text-align:center}
.list{position:absolute;list-style:none;font-size:19px;line-height:28px;color:var(--ink);white-space:nowrap}
.list li{padding-left:24px;position:relative}
.list li::before{content:"";position:absolute;left:0;top:8px;width:13px;height:13px;border-radius:50%;background:var(--navy)}
.list li::after{content:"";position:absolute;left:3px;top:11px;width:6px;height:3px;border-left:2px solid #fff;border-bottom:2px solid #fff;transform:rotate(-45deg)}
.list--sky li::before{background:var(--sky)}
.dur{position:absolute;font-weight:700;color:var(--navy);font-size:19px}
.date{position:absolute;font-weight:700;color:var(--sky);font-size:38px;line-height:1;word-spacing:10px}
</style>
</head>
<body>

<section class="page page--front">
  <div class="abs" style="left:0;top:200px;width:831px;height:395px;background:var(--sky)"></div>
  <div class="photo" role="img" aria-label="Modern glass office with people at a meeting table" style="left:0;top:0;width:831px;height:280px;clip-path:polygon(0 0,100% 0,100% 74%,75% 94%,62% 100%,0 66%)"></div>
  <svg class="abs" style="left:0;top:170px" width="831" height="120" viewBox="0 0 831 120">
    <path d="M0 18 L620 95 Q650 100 680 92 L831 40 L831 0 L831 40 L690 100 Q640 112 600 104 L0 60Z" fill="#fff"/>
  </svg>
  <svg class="abs" style="left:775px;top:265px" width="34" height="50"><g fill="#fff">
    <circle cx="3" cy="3" r="2"/><circle cx="17" cy="3" r="2"/><circle cx="31" cy="3" r="2"/>
    <circle cx="3" cy="17" r="2"/><circle cx="17" cy="17" r="2"/><circle cx="31" cy="17" r="2"/>
    <circle cx="3" cy="31" r="2"/><circle cx="17" cy="31" r="2"/><circle cx="31" cy="31" r="2"/>
    <circle cx="3" cy="45" r="2"/><circle cx="17" cy="45" r="2"/><circle cx="31" cy="45" r="2"/></g></svg>

  <h1 class="abs" style="left:82px;top:282px;color:#fff;font-family:'Bebas Neue',sans-serif;font-weight:400;font-size:60px;line-height:1">SKILL UP, SALARY UP</h1>
  <h2 class="abs" style="left:82px;top:338px;color:#fff;font-family:'Oswald',sans-serif;font-weight:700;font-size:52px;line-height:1.05">UPCOMING HLC COURSES</h2>
  <p class="abs" style="left:87px;top:405px;color:#fff;font-weight:600;font-size:20px">MEN &amp; WOMEN • IN-PERSON &amp; REMOTE • PARTIAL SCHOLORASHIPS</p>

  <article class="card" style="left:43px;top:458px;width:356px;height:564px">
    <h3 class="card__title">Harbor Lantern<br>Course</h3>
    <p class="abs blue" style="left:32px;top:100px;font-weight:700;font-size:18px">Business Skills &amp; Knowledge to:</p>
    <ul class="list list--sky" style="left:32px;top:126px;font-weight:600;font-size:17px;line-height:26px"><li>Impress your interviewer</li><li>Maxi mize Income</li></ul>
    <div class="outline" style="left:27px;top:194px;width:303px;height:38px;font-size:19px;line-height:34px">Start / Run Your Business</div>
    <p class="dur" style="left:30px;top:250px">4-5 MONTHS</p>
    <p class="date" style="left:28px;top:273px">NOV 2025</p>
    <div class="tag" style="left:27px;top:326px;width:303px;height:40px;font-size:25px;line-height:40px">Partial Listing</div>
    <ul class="list" style="left:27px;top:372px"><li>Computers</li><li>Marketing</li><li>Sales</li><li>Finance</li><li>Business<br>Strategy</li></ul>
    <ul class="list" style="left:168px;top:372px"><li>Healthcare</li><li>Communication</li><li>LedgerPro</li><li>Investments</li><li>Real Estate</li><li>Accounting</li></ul>
  </article>

  <div class="card" style="left:427px;top:455px;width:367px;height:178px;padding:6px">
    <div class="photo" role="img" aria-label="Team of colleagues collaborating around a laptop in an office" style="position:relative;width:100%;height:100%;border-radius:12px;background:linear-gradient(135deg,#cdbba6,#8c7e74 50%,#3a4658)"></div>
  </div>

  <article class="card" style="left:432px;top:650px;width:357px;height:372px">
    <h3 class="card__title">Software,<br>Web &amp; Apps</h3>
    <p class="abs blue" style="left:25px;top:100px;font-weight:700;font-size:25px">#2 Best Tech Job</p>
    <p class="abs amber" style="left:25px;top:133px;font-weight:500;font-size:17px">National Careers Review 2025</p>
    <div class="tag" style="left:28px;top:168px;width:303px;height:40px;font-size:25px;line-height:40px">Job Prerequisite</div>
    <ul class="list" style="left:28px;top:212px"><li>Computer Programmer</li><li>Software Developer/Mobile ·</li><li>Engineer Developer (Apps</li></ul>
    <p class="date" style="left:26px;top:317px">NOV 2025</p>
  </article>

  <div class="abs" style="left:0;top:1080px;width:410px;height:20px;background:var(--navy);clip-path:polygon(0 0,100% 0,98% 100%,0 100%)"></div>
  <div class="abs" style="left:418px;top:1080px;width:413px;height:20px;background:var(--sky);clip-path:polygon(2% 0,100% 0,100% 100%,0 100%)"></div>
</section>

<section class="page page--back">
  <div class="abs" style="left:0;top:0;width:831px;height:238px;background:var(--sky)"></div>

  <article class="card" style="left:43px;top:53px;width:357px;height:372px">
    <h3 class="card__title">Bookkeeping<br>LedgerPro</h3>
    <p class="abs" style="left:34px;top:95px;font-weight:700;font-size:22px;color:var(--ink)">Train for a quality job</p>
    <p class="abs blue" style="left:34px;top:120px;font-weight:700;font-size:22px">Manage your own books</p>
    <div class="abs" style="left:34px;top:160px;width:288px;height:2px;background:var(--amber)"></div>
    <ul class="list" style="left:34px;top:177px"><li>Finance Management</li><li>Customer &amp; Vendor Mgmt.</li><li>Advanced Tools</li></ul>
    <p class="dur" style="left:34px;top:285px">5 WEEKS</p>
    <p class="date" style="left:32px;top:310px">NOV 2025</p>
  </article>

  <article class="card" style="left:430px;top:53px;width:358px;height:372px">
    <h3 class="card__title" style="font-size:25px;line-height:26px;padding:13px 0 12px 16px">IT Desktop &amp;<br>Networking Support</h3>
    <p class="abs blue" style="left:24px;top:93px;font-weight:700;font-size:25px">#2 Best Tech Job</p>
    <p class="abs amber" style="left:24px;top:125px;font-weight:500;font-size:17px">National Careers Review 2025</p>
    <div class="tag" style="left:28px;top:161px;width:302px;height:40px;font-size:25px;line-height:40px">Masters it:</div>
    <ul class="list" style="left:28px;top:208px"><li>Paneos</li><li>Networks</li></ul>
    <ul class="list" style="left:165px;top:208px"><li>Servers</li><li>Cloud</li></ul>
    <p class="dur" style="left:28px;top:287px">7 MONTHS</p>
    <p class="date" style="left:26px;top:310px">DEC 2025</p>
  </article>

  <div class="photo" role="img" aria-label="Smiling man in a white collared shirt with arms crossed in a bright office" style="left:0;top:458px;width:400px;height:540px;border-top-right-radius:30px;background:linear-gradient(160deg,#e7ecef,#c9d4da 45%,#b7a89b)"></div>

  <article class="card" style="left:430px;top:458px;width:358px;height:357px">
    <h3 class="card__title" style="padding-left:20px">Brightdesk Office-<br>Computers</h3>
    <p class="abs amber" style="left:36px;top:95px;font-weight:700;font-size:18px">THE NEW JOB PREREQUISITE</p>
    <ul class="list" style="left:36px;top:135px"><li>Gridcalc</li><li>Docwise</li></ul>
    <ul class="list" style="left:168px;top:135px"><li>Mailpost</li><li>Slidecraft</li></ul>
    <div class="outline" style="left:27px;top:203px;width:303px;height:36px;font-size:16px;line-height:32px">Computer lab available to practice</div>
    <p class="dur" style="left:36px;top:280px">5 WEEKS</p>
    <p class="date" style="left:34px;top:302px">DEC 2025</p>
  </article>

  <p class="abs navy" style="left:445px;top:873px;font-weight:600;font-size:18px;line-height:23px">MEN &amp; WOMEN • IN-PERSON &amp;<br>REMOTE • PARTIAL SCHOLORASHIPS</p>

  <div class="abs" style="left:0;top:990px;width:430px;height:90px;background:var(--sky);clip-path:polygon(0 0,100% 0,93% 100%,0 100%)"></div>
  <div class="abs" style="left:400px;top:972px;width:431px;height:128px;background:var(--navy);clip-path:polygon(8% 0,100% 0,100% 100%,0 100%)"></div>
  <div class="abs" style="left:0;top:1080px;width:831px;height:20px;background:var(--navy)"></div>

  <svg class="abs" style="left:66px;top:1015px" width="30" height="40" viewBox="0 0 24 32"><path d="M5 2 L10 2 L12 9 L8 12 Q10 19 14 23 L18 20 L23 24 L22 29 Q18 32 12 27 Q3 18 2 8 Q2 3 5 2Z" fill="#fff"/></svg>
  <p class="abs" style="left:98px;top:1000px;color:#fff;font-family:'Oswald',sans-serif;font-weight:700;font-size:50px;line-height:1.3">555-014-2290</p>

  <svg class="abs" style="left:450px;top:1002px" width="22" height="22" viewBox="0 0 22 22"><circle cx="11" cy="11" r="9" fill="none" stroke="#fff" stroke-width="2"/><path d="M2 11h18M11 2q-5 9 0 18M11 2q5 9 0 18" fill="none" stroke="#fff" stroke-width="1.6"/></svg>
  <p class="abs" style="left:480px;top:993px;color:#fff;font-weight:700;font-size:28px">info@hlcourses.com</p>
  <svg class="abs" style="left:450px;top:1036px" width="22" height="22" viewBox="0 0 22 22"><circle cx="11" cy="11" r="9" fill="none" stroke="#fff" stroke-width="2"/><rect x="6" y="7.5" width="10" height="7" fill="none" stroke="#fff" stroke-width="1.5"/><path d="M6 8l5 4 5-4" fill="none" stroke="#fff" stroke-width="1.5"/></svg>
  <p class="abs" style="left:480px;top:1027px;color:#fff;font-weight:700;font-size:28px">www.hlcourses.com</p>
</section>

</body>
</html>
```